Fennick Executive Search - New Business Card Design Project

We are an executive search firm called Fennick Executive Search based in the UK. We require a custom design for a business card. We're looking to convey a professional service to executives for executive search recruitment services. In terms of colours, we like dark blues and grays (maybe even silver incorporated somewhere if we go for a foiled type of card) but we're open to your artistic flare. See our current logo in attachments. We are totally open on design so long as the design is slick and professional.
Updates

Thanks for all your contributions of various designs. I have to say the quality of work has been amazing which is going to make our job quite difficult in the coming days on making a decision. Thanks to you all that have taken the time to submit designs thus far. We'll keep on reviewing and try to narrow down our selection as soon as possible.

Target Market(s)

Executive Search

Industry/Entity Type

Recruitment

Contact Information for Business Card

Fennick Executive Search,
Exclusively Sourcing & Hiring Senior Leaders
Gordon Pellbury, Managing Director,
07823 906417
0117 486 7132
gordon@fennickexecutive.co.uk
fennickexecutive.co.uk
58 Lindmoor Court, Hatherley Road, Bristol, BS32 9QJ

Font styles to use
Sans Serif
Other font styles liked:
• Roboto (which is used in our logo)

Requirements
Must have
• Our logo (It has a subtle fade on it from #02071d at top to #333649 at bottom)
• The logo can be on one side or both sides
• Must be elegant and professional
• We have 2nd slogan CONSULT | INSPIRE | INNOVATE | DELIVER which can be incorporated into the card
Nice to have
• Use of blues and grey colours
• Compatible with similar styling to our website fennickexecutive.co.uk
Should not have
• Must not be overly brash
• Must not contain cartoon characters

```html
<!DOCTYPE html>
<html lang="en">
<head>
<meta charset="utf-8">
<title>Fennick Executive Search – Business Card</title>
<link rel="stylesheet" href="https://fonts.googleapis.com/css2?family=Roboto:wght@500&family=Open+Sans:wght@400;700&display=swap">
<style>
  :root {
    --bg: #3a3a3c;
    --navy-top: #1e2a52;
    --navy-mid: #1a2446;
    --navy-deep: #131a36;
    --white: #ffffff;
    --silver: #d8dbe3;
  }
  * { box-sizing: border-box; margin: 0; padding: 0; }
  html, body { width: 1200px; height: 900px; overflow: hidden; }
  body {
    background: var(--bg);
    font-family: "Open Sans", Arial, sans-serif;
    color: var(--white);
    position: relative;
  }
  .card {
    position: absolute;
    width: 620px;
    height: 354px;
    border-radius: 22px;
    overflow: hidden;
    box-shadow: 0 14px 30px rgba(0,0,0,.45);
  }
  .card-front {
    left: 150px; top: 70px;
    background: radial-gradient(ellipse at 50% 40%, var(--navy-top) 0%, var(--navy-mid) 55%, var(--navy-deep) 100%);
  }
  .card-back {
    left: 430px; top: 470px;
    background: radial-gradient(ellipse at 40% 30%, var(--navy-top) 0%, var(--navy-mid) 55%, var(--navy-deep) 100%);
  }
  .wordmark {
    font-family: "Roboto", Arial, sans-serif;
    font-weight: 500;
    color: var(--white);
    letter-spacing: .5px;
    white-space: nowrap;
  }
  .front-brand {
    position: absolute;
    left: 0; right: 0; top: 96px;
    text-align: center;
  }
  .front-brand .wordmark { font-size: 36px; }
  .front-tagline {
    margin-top: 8px;
    font-size: 14px;
    color: var(--silver);
  }
  .front-slogan {
    position: absolute;
    left: 0; right: 0; top: 236px;
    text-align: center;
    font-size: 15px;
    letter-spacing: .6px;
    color: var(--silver);
  }
  .back-brand {
    position: absolute;
    right: 32px; top: 34px;
  }
  .back-brand .wordmark { font-size: 24px; }
  .person {
    position: absolute;
    left: 30px; top: 84px;
    padding-left: 22px;
  }
  .person::before {
    content: "";
    position: absolute;
    left: 0; top: 2px;
    width: 9px; height: 46px;
    background: var(--white);
  }
  .person-name { font-size: 23px; line-height: 1.1; }
  .person-name strong { font-weight: 700; }
  .person-role { font-size: 13px; color: var(--silver); }
  .contacts {
    position: absolute;
    left: 34px; top: 172px;
    list-style: none;
    font-size: 14px;
    color: var(--silver);
  }
  .contacts li {
    display: flex;
    align-items: center;
    gap: 10px;
    height: 25px;
  }
  .contacts svg { width: 14px; height: 14px; fill: var(--white); flex: none; }
  .divider {
    position: absolute;
    left: 0; top: 0;
    width: 620px; height: 354px;
  }
  .website {
    position: absolute;
    left: 34px; top: 314px;
    font-size: 15px;
    color: var(--silver);
  }
</style>
</head>
<body>

  <section class="card card-front">
    <div class="front-brand">
      <div class="wordmark">Fennick Executive Search</div>
      <div class="front-tagline">Exclusively Sourcing &amp; Hiring Senior Leaders</div>
    </div>
    <div class="front-slogan">CONSULT | INSPIRE | INNOVATE | DELIVER</div>
  </section>

  <section class="card card-back">
    <div class="back-brand">
      <div class="wordmark">Fennick Executive Search</div>
    </div>

    <div class="person">
      <div class="person-name">Gordon <strong>Pellbury</strong></div>
      <div class="person-role">Managing Director</div>
    </div>

    <ul class="contacts">
      <li>
        <svg viewBox="0 0 16 16" aria-hidden="true"><path d="M3 2h3l1.5 3.5-2 1.3a8 8 0 0 0 3.7 3.7l1.3-2L14 10v3a1 1 0 0 1-1 1C7 14 2 9 2 3a1 1 0 0 1 1-1z"/></svg>
        07823 906417
      </li>
      <li>
        <svg viewBox="0 0 16 16" aria-hidden="true"><path d="M3 2h3l1.5 3.5-2 1.3a8 8 0 0 0 3.7 3.7l1.3-2L14 10v3a1 1 0 0 1-1 1C7 14 2 9 2 3a1 1 0 0 1 1-1z"/></svg>
        0117 486 7132
      </li>
      <li>
        <svg viewBox="0 0 16 16" aria-hidden="true"><path d="M1 3h14v10H1z M1.8 3.6 8 8.6l6.2-5v1.3L8 9.9 1.8 4.9z" fill-rule="evenodd"/></svg>
        gordon@fennickexecutive.co.uk
      </li>
      <li>
        <svg viewBox="0 0 16 16" aria-hidden="true"><path d="M8 1a5 5 0 0 1 5 5c0 3.5-5 9-5 9S3 9.5 3 6a5 5 0 0 1 5-5zm0 3a2 2 0 1 0 0 4 2 2 0 0 0 0-4z" fill-rule="evenodd"/></svg>
        58 Lindmoor Court, Hatherley Road, Bristol, BS32 9QJ
      </li>
    </ul>

    <svg class="divider" viewBox="0 0 620 354" aria-hidden="true">
      <polyline points="0,302 478,302 496,288 620,288" fill="none" stroke="#ffffff" stroke-width="2"/>
      <rect x="496" y="284" width="124" height="5" fill="#ffffff"/>
    </svg>

    <div class="website">fennickexecutive.co.uk</div>
  </section>

</body>
</html>
```